A WEBSITE FOR A JEWELLERY RETAIL STORE WITH A SHOPPING CART, AND ABILITY TO ORDER ONLINE.

I require a website with a shopping cart.

We sell MAINLY diamond jewellery (such as rings etc). I need it to be simple to change prices with only a few buttons, as the price fluctuates due to the US Dollar.

We are a diamond wholesaler, selling directly to the public, so we guarantee the lowest prices in Australia.

There is also a link to current inventory that will need to be uploaded to the site.

This could be an ongoing job, where you will be paid weekly to maintain and update the website if you wish.

Target Market(s)

People getting engaged, and wanting to buy a diamond ring.

Number of Pages Required

5+ page

Colors

Designer to choose colors to be used in the design.

Requirements
Must have
• elegant.
• modern.
• professional.
• SHOPPING CART.
• ABILITY TO SEARCH FOR LOOSE DIAMONDS (LINK THAT NEEDS TO BE EMBEDDED WILL BE SENT WHICH SHOWS CURRENT STOCK).
• ENGAGEMENT RINGS
• WEDDING RINGS
• DIAMOND EARRINGS
• DIAMOND PENDANTS
• LOOSE DIAMONDS.
• SALE ITEMS.
• OTHER JEWELLERY.
• EDUCATION
• WISH LIST
• CART.
Nice to have
• a good place to look for inspiration on pages is https://www.lumenvael.example.
• YOU MAY VISIT OUR FACEBOOK PAGE AT.
• HTTP://WWW.SOCIALPAGE.EXAMPLE/QUILLSTONEJEWELLERS
Should not have
• We don't want it too busy.

```html
<!DOCTYPE html>
<html lang="en">
<head>
<meta charset="utf-8">
<title>Quillstone Jewellers</title>
<link rel="stylesheet" href="https://fonts.googleapis.com/css2?family=Bodoni+Moda:wght@600&family=Maven+Pro:wght@400;500&family=Roboto:wght@300&display=swap">
<style>
  :root {
    --ink: #1a1919;
    --bar: #1d1b1a;
    --gold: #b8884a;
    --gold-bright: #e9b54c;
    --gold-soft: #f1c877;
    --card-head: #5b4b40;
    --panel: rgba(80, 68, 60, 0.92);
    --white: #ffffff;
  }
  * { box-sizing: border-box; margin: 0; padding: 0; }
  html, body { width: 1097px; height: 1200px; overflow: hidden; background: var(--ink); }
  body { position: relative; font-family: "Maven Pro", sans-serif; color: var(--white); }

  .hero-photo {
    position: absolute; left: 0; top: 0; width: 1097px; height: 746px;
    background:
      radial-gradient(ellipse 420px 300px at 640px 360px, #b88a6c 0%, rgba(150,110,85,0.6) 45%, rgba(0,0,0,0) 80%),
      linear-gradient(160deg, #3c302b 0%, #6e5a4d 40%, #8a6e5c 60%, #5e4a3f 100%);
  }
  .top-bar {
    position: absolute; left: 0; top: 0; width: 1097px; height: 37px;
    background: var(--bar); display: flex; align-items: center;
  }
  .phone { position: absolute; left: 103px; top: 7px; display: flex; align-items: center; gap: 10px; color: var(--gold); font-size: 17px; letter-spacing: 0.5px; }
  .account { position: absolute; left: 786px; top: 8px; display: flex; gap: 24px; color: var(--gold); font-size: 17px; font-weight: 500; letter-spacing: 0.6px; }
  .flag { position: absolute; left: 964px; top: 7px; }

  .main-nav {
    position: absolute; left: 0; top: 37px; width: 1097px; height: 85px;
    background: rgba(30, 26, 24, 0.55);
  }
  .brand { position: absolute; left: 103px; top: 16px; display: flex; align-items: center; gap: 10px; color: var(--white); }
  .brand-mark { width: 42px; height: 46px; background: var(--white); }
  .brand-name { font-family: "Maven Pro", sans-serif; font-weight: 400; font-size: 26px; letter-spacing: 1px; line-height: 1; }
  .brand-name span { display: block; font-size: 14px; letter-spacing: 9px; margin-top: 6px; }
  .nav-links { position: absolute; top: 28px; left: 511px; display: flex; gap: 0; font-size: 17px; color: var(--gold-soft); }
  .nav-links li { list-style: none; display: flex; align-items: center; gap: 3px; }
  .nav-links li + li { margin-left: 22px; }

  .hero-title {
    position: absolute; left: 0; top: 285px; width: 1097px; text-align: center;
    font-family: "Bodoni Moda", serif; font-weight: 600; font-size: 56px; letter-spacing: 0.5px;
  }
  .hero-sub {
    position: absolute; left: 0; top: 378px; width: 1097px; text-align: center;
    font-family: "Roboto", sans-serif; font-weight: 300; font-size: 27px; letter-spacing: 1.5px;
  }
  .hero-btn {
    position: absolute; top: 458px; width: 198px; height: 61px;
    border: 2px solid var(--gold-bright); display: flex; align-items: center; justify-content: center;
    font-size: 15px; font-weight: 500; letter-spacing: 1px; color: var(--white);
  }
  .side-tab {
    position: absolute; left: 1034px; width: 63px; height: 64px; background: var(--panel);
    display: flex; align-items: center; justify-content: center;
  }
  .search-panel { position: absolute; left: 850px; top: 459px; width: 247px; height: 64px; background: var(--panel); }
  .search-field {
    position: absolute; left: 25px; top: 12px; width: 187px; height: 41px;
    border: 2px solid var(--gold-bright); border-radius: 21px;
    padding-left: 18px; line-height: 37px; color: #a2968c; font-size: 15px; letter-spacing: 1px;
  }

  .collection {
    position: absolute; left: 0; top: 746px; width: 1097px; height: 310px; background: var(--ink);
  }
  .product-card {
    position: absolute; top: 698px; width: 203px; height: 264px;
    border: 2px solid var(--gold-bright); background: var(--white);
    box-shadow: 0 0 6px rgba(233,181,76,0.5);
  }
  .product-card h3 {
    height: 51px; background: var(--card-head); color: var(--white);
    font-weight: 500; font-size: 15px; letter-spacing: 1px; text-align: center; line-height: 51px;
  }
  .product-photo {
    margin: 24px auto 0; width: 180px; height: 150px;
    background: radial-gradient(ellipse 80px 60px at 50% 50%, #e8ebf0 0%, #f6f7f9 60%, #ffffff 100%);
  }
  .product-photo.gold { background: radial-gradient(ellipse 80px 60px at 50% 50%, #eef0f3 0%, #f4ecd0 55%, #ffffff 100%); }

  .story {
    position: absolute; left: 0; top: 1056px; width: 1097px; height: 144px;
    background: linear-gradient(90deg, #4d5150 0%, #8c9392 35%, #6b6260 55%, #aab3b1 75%, #c2c9c8 100%);
  }
  .story-title {
    position: absolute; left: 56px; top: 1073px;
    font-family: "Bodoni Moda", serif; font-weight: 600; font-size: 44px; color: var(--white);
  }
</style>
</head>
<body>
  <div class="hero-photo" role="img" aria-label="Photograph of two hands, one wearing a diamond engagement ring"></div>

  <header class="top-bar">
    <div class="phone">
      <svg width="18" height="18" viewBox="0 0 24 24" aria-hidden="true"><path fill="#b8884a" d="M6.6 10.8a15 15 0 0 0 6.6 6.6l2.2-2.2c.3-.3.7-.4 1-.2 1.1.4 2.3.6 3.6.6.6 0 1 .4 1 1V20c0 .6-.4 1-1 1A17 17 0 0 1 3 4c0-.6.4-1 1-1h3.5c.6 0 1 .4 1 1 0 1.3.2 2.5.6 3.6.1.3 0 .7-.2 1z"/></svg>
      (800) 555-0142
    </div>
    <div class="account"><span>LOGIN</span><span>SIGN UP</span></div>
    <svg class="flag" width="30" height="20" viewBox="0 0 30 20" aria-label="United States region">
      <rect width="30" height="20" fill="#ffffff"/>
      <g fill="#c9302c"><rect y="0" width="30" height="2"/><rect y="4" width="30" height="2"/><rect y="8" width="30" height="2"/><rect y="12" width="30" height="2"/><rect y="16" width="30" height="2"/></g>
      <rect width="13" height="10" fill="#2b3f8c"/>
    </svg>
  </header>

  <nav class="main-nav">
    <div class="brand">
      <div class="brand-mark"></div>
      <div class="brand-name">QUILLSTONE<span>JEWELLERS</span></div>
    </div>
    <ul class="nav-links">
      <li>Diamonds<svg width="14" height="8" viewBox="0 0 14 8"><path d="M1 1l6 6 6-6" fill="none" stroke="#f1c877" stroke-width="1.3"/></svg></li>
      <li>Rings<svg width="14" height="8" viewBox="0 0 14 8"><path d="M1 1l6 6 6-6" fill="none" stroke="#f1c877" stroke-width="1.3"/></svg></li>
      <li>Earrings<svg width="14" height="8" viewBox="0 0 14 8"><path d="M1 1l6 6 6-6" fill="none" stroke="#f1c877" stroke-width="1.3"/></svg></li>
      <li>Others<svg width="14" height="8" viewBox="0 0 14 8"><path d="M1 1l6 6 6-6" fill="none" stroke="#f1c877" stroke-width="1.3"/></svg></li>
      <li>Eductation</li>
    </ul>
  </nav>

  <h1 class="hero-title">You Design It we Build It</h1>
  <p class="hero-sub">Create your own unique diamond engagement ring.</p>
  <a class="hero-btn" style="left:326px">Engagement Rings</a>
  <a class="hero-btn" style="left:573px">Loose Diamonds</a>

  <div class="side-tab" style="top:284px" aria-label="Wish list">
    <svg width="38" height="34" viewBox="0 0 38 34"><path d="M19 31S3 21 3 11a8 8 0 0 1 16-3 8 8 0 0 1 16 3c0 10-16 20-16 20z" fill="none" stroke="#e9b54c" stroke-width="2.2"/></svg>
  </div>
  <div class="side-tab" style="top:372px" aria-label="Cart">
    <svg width="42" height="38" viewBox="0 0 42 38"><path d="M2 4h6l5 20h22l4-14H11" fill="none" stroke="#e9b54c" stroke-width="2.2"/><circle cx="17" cy="32" r="2.6" fill="none" stroke="#e9b54c" stroke-width="2"/><circle cx="31" cy="32" r="2.6" fill="none" stroke="#e9b54c" stroke-width="2"/></svg>
  </div>
  <div class="search-panel"><div class="search-field">search</div></div>

  <section class="collection"></section>
  <article class="product-card" style="left:71px"><h3>Engagement Ring</h3><div class="product-photo" role="img" aria-label="Oval diamond solitaire ring in white gold"></div></article>
  <article class="product-card" style="left:322px"><h3>Wedding Ring</h3><div class="product-photo" role="img" aria-label="Oval halo diamond ring with pavé band"></div></article>
  <article class="product-card" style="left:565px"><h3>Diamond Earrings</h3><div class="product-photo" role="img" aria-label="Oval diamond jewellery piece"></div></article>
  <article class="product-card" style="left:813px"><h3>Engagement Ring</h3><div class="product-photo gold" role="img" aria-label="Round halo diamond ring in yellow gold"></div></article>

  <section class="story" role="img" aria-label="Photograph of an engaged couple outdoors"></section>
  <h2 class="story-title">You Design It, We Build It</h2>
</body>
</html>
```